Bref créative
Cool Cards for Engineering and design business
Borealis Drafting and Systems Inc.
Professional
Derek Wolfe
President
#22 - 3407 6th street
Corvallen, Wr
T4R 2K9
derek.wolfe@borealisdraftsys.ca
www.borealisdraftsys.ca
Please use clear standard font. We can try some with the logo font. I want the card to be modern POP and stand out.
Please put a QR code on the back with the contact info. I want this designed so it is optional and can be printed as a single card too.

```html
<!DOCTYPE html>
<html lang="en">
<head>
<meta charset="utf-8">
<title>Borealis Drafting and Systems Inc. – Business Card</title>
<link href="https://fonts.googleapis.com/css2?family=Michroma&display=swap" rel="stylesheet">
<style>
  :root {
    --page-bg: #e9e7e4;
    --card-white: #ffffff;
    --charcoal: #3b3b3d;
    --charcoal-deep: #2a2a2c;
    --green: #3fb52c;
    --green-light: #8fd97e;
    --text-light: #e4e4e4;
    --icon-fill: #f2f2f2;
  }
  * { box-sizing: border-box; margin: 0; padding: 0; }
  html, body {
    width: 1200px; height: 900px; overflow: hidden;
    background: var(--page-bg);
    font-family: "Michroma", sans-serif;
  }
  .canvas {
    position: relative; width: 1200px; height: 900px;
    display: flex; align-items: center; justify-content: center;
  }
  .card {
    position: relative; width: 1000px; height: 570px;
    background: var(--card-white);
    box-shadow: 0 12px 30px rgba(0,0,0,0.18);
    overflow: hidden;
  }
  .card-art { position: absolute; inset: 0; }
  .brand {
    position: absolute; left: 350px; top: 62px;
    display: flex; align-items: center; gap: 18px;
    color: var(--green);
  }
  .brand-dot {
    width: 58px; height: 58px; border-radius: 50%;
    background: var(--green); flex: none;
  }
  .brand-name { line-height: 1.25; }
  .brand-name .primary { display: block; font-size: 40px; letter-spacing: 2px; text-transform: uppercase; }
  .brand-name .secondary { display: block; font-size: 13px; letter-spacing: 1px; text-transform: uppercase; }
  .contact {
    position: absolute; left: 34px; top: 372px;
    list-style: none; color: var(--text-light);
    font-size: 13px; letter-spacing: 0.5px; text-transform: uppercase;
  }
  .contact li { display: flex; align-items: flex-start; gap: 9px; margin-bottom: 6px; line-height: 1.35; }
  .contact .lower { text-transform: lowercase; }
  .contact svg { flex: none; width: 16px; height: 16px; margin-top: 1px; }
  .person {
    position: absolute; right: 52px; top: 340px;
    color: var(--text-light); text-align: center;
    text-transform: uppercase;
  }
  .person-name { font-size: 20px; letter-spacing: 2px; }
  .person-title { font-size: 15px; letter-spacing: 1.5px; margin-top: 10px; }
</style>
</head>
<body>
<main class="canvas">
  <section class="card" aria-label="Business card front">
    <svg class="card-art" viewBox="0 0 1000 570" preserveAspectRatio="none" aria-hidden="true">
      <defs>
        <linearGradient id="darkPanel" x1="0" y1="0" x2="0" y2="1">
          <stop offset="0" stop-color="var(--charcoal)"/>
          <stop offset="1" stop-color="var(--charcoal-deep)"/>
        </linearGradient>
      </defs>
      <path class="swoosh-light" d="M0 300 C 220 330, 420 330, 600 270 C 760 215, 900 220, 1000 250 L1000 275 C 880 250, 740 255, 600 300 C 420 355, 200 350, 0 330 Z" fill="var(--green-light)" opacity="0.7"/>
      <path class="swoosh-main" d="M0 318 C 240 360, 440 350, 620 290 C 780 238, 900 240, 1000 268 L1000 292 C 900 268, 780 272, 630 318 C 450 372, 230 380, 0 350 Z" fill="var(--green)"/>
      <path class="dark-panel" d="M0 345 C 230 385, 450 375, 630 318 C 780 272, 900 270, 1000 292 L1000 570 L0 570 Z" fill="url(#darkPanel)"/>
    </svg>

    <div class="brand">
      <span class="brand-dot"></span>
      <span class="brand-name">
        <span class="primary">Borealis</span>
        <span class="secondary">Drafting and Systems Inc.</span>
      </span>
    </div>

    <ul class="contact">
      <li>
        <svg viewBox="0 0 16 16"><circle cx="8" cy="8" r="8" fill="var(--icon-fill)"/><path d="M8 3.5a3 3 0 0 0-3 3c0 2.2 3 6 3 6s3-3.8 3-6a3 3 0 0 0-3-3z" fill="var(--charcoal)"/><circle cx="8" cy="6.5" r="1" fill="var(--icon-fill)"/></svg>
        <span>#22 - 3407 6th street Corvallen,<br>Wr T4R 2K9</span>
      </li>
      <li>
        <svg viewBox="0 0 16 16"><circle cx="8" cy="8" r="8" fill="var(--icon-fill)"/><path d="M5.2 4h1.7l.8 2-1 .8a5 5 0 0 0 2.5 2.5l.8-1 2 .8v1.7c-4 .5-7.3-2.8-6.8-6.8z" fill="var(--charcoal)"/></svg>
        <span>780-555-0142</span>
      </li>
      <li>
        <svg viewBox="0 0 16 16"><circle cx="8" cy="8" r="8" fill="var(--icon-fill)"/><path d="M5.2 4h1.7l.8 2-1 .8a5 5 0 0 0 2.5 2.5l.8-1 2 .8v1.7c-4 .5-7.3-2.8-6.8-6.8z" fill="var(--charcoal)"/></svg>
        <span>780-555-0187</span>
      </li>
      <li>
        <svg viewBox="0 0 16 16"><circle cx="8" cy="8" r="8" fill="var(--icon-fill)"/><path d="M5.2 4h1.7l.8 2-1 .8a5 5 0 0 0 2.5 2.5l.8-1 2 .8v1.7c-4 .5-7.3-2.8-6.8-6.8z" fill="var(--charcoal)"/></svg>
        <span>780-555-0163</span>
      </li>
      <li>
        <svg viewBox="0 0 16 16"><circle cx="8" cy="8" r="8" fill="var(--icon-fill)"/><rect x="4" y="5" width="8" height="6" fill="var(--charcoal)"/><path d="M4 5l4 3 4-3" stroke="var(--icon-fill)" stroke-width="0.8" fill="none"/></svg>
        <span class="lower">derek.wolfe@borealisdraftsys.ca</span>
      </li>
      <li>
        <svg viewBox="0 0 16 16"><circle cx="8" cy="8" r="8" fill="var(--icon-fill)"/><circle cx="8" cy="8" r="4" fill="none" stroke="var(--charcoal)" stroke-width="1"/><path d="M4 8h8M8 4c-1.6 2.2-1.6 5.8 0 8M8 4c1.6 2.2 1.6 5.8 0 8" stroke="var(--charcoal)" stroke-width="0.8" fill="none"/></svg>
        <span class="lower">www.borealisdraftsys.ca</span>
      </li>
    </ul>

    <div class="person">
      <p class="person-name">Derek Wolfe</p>
      <p class="person-title">President</p>
    </div>
  </section>
</main>
</body>
</html>
```